FLYERENTWURF  für Make up Ausbildung
FLYERENTWURF für Make up Ausbildung
Zielgruppe
friseure die sich weiterbilden wollen
Aufgabenstellung
zu entwerfen ist ein doppelseitiger flyer in A4, zweimal gefalten.
außenseite:
erste spalte/deckblatt:
das logo (im anhang)
schriftzug: mira beauty schule
eventuell bild kussmund, wenn rechte vorhanden.
zweite spalte/hinterseite:
zahlungsbedingungen (text wird noch beigefügt)
dritte spalte:
personenbild (anhang)
personenbeschreibung (text wird noch beigefügt)
innenseite:
text aus anhang

```html
<!DOCTYPE html>
<html lang="de">
<head>
<meta charset="utf-8">
<title>mira beauty schule – Flyer Außenseite</title>
<link href="https://fonts.googleapis.com/css2?family=Carlito&family=Comfortaa:wght@400;600&display=swap" rel="stylesheet">
<style>
  :root{
    --black:#000000;
    --white:#ffffff;
    --magenta:#a3114f;
    --star-grey:#a9a9ab;
    --text-light:#f2f2f2;
    --skin-light:#f0d9c8;
    --skin-mid:#d9a58e;
    --hair-blond:#efe6d2;
    --dress-plum:#5a4a58;
  }
  *{margin:0;padding:0;box-sizing:border-box}
  html,body{width:1200px;height:848px;overflow:hidden;background:var(--white)}
  .flyer{position:relative;width:1200px;height:848px;overflow:hidden;background:var(--black)}

  /* left column: profile */
  .profile-name{position:absolute;left:37px;top:46px;font-family:"Comfortaa",sans-serif;font-weight:600;font-size:19px;color:var(--white);letter-spacing:.3px}
  .portrait{position:absolute;left:35px;top:105px;width:168px;height:217px;border:4px solid var(--magenta);border-radius:12px;overflow:hidden;background:linear-gradient(180deg,#e6e1d8 0%,#cdb9aa 55%,#2a2424 100%)}
  .portrait-reflection{position:absolute;left:35px;top:326px;width:168px;height:80px;border-radius:12px;background:linear-gradient(180deg,rgba(60,55,55,.55) 0%,rgba(0,0,0,0) 100%)}
  .stars-left{position:absolute;left:132px;top:182px}
  .profile-text{position:absolute;left:30px;top:458px;width:330px;font-family:"Carlito",sans-serif;font-size:12.4px;line-height:15.4px;color:var(--text-light);hyphens:auto;-webkit-hyphens:auto}
  .profile-text p{margin-bottom:15.4px}
  .profile-text p:last-child{margin-bottom:0}

  /* divider lines */
  .rule{position:absolute;top:0}
  .rule--magenta{left:407px;width:5px;height:428px;background:var(--magenta)}
  .rule--white{left:414px;width:4px;height:307px;background:var(--white)}

  /* middle column: detail photos */
  .detail{position:absolute;left:468px;width:262px;height:174px;border-radius:14px}
  .detail--lips{top:88px;background:radial-gradient(ellipse at 50% 45%,#c8866f 0%,#e2b39c 45%,#f3d8c7 100%)}
  .detail--eyes{top:339px;background:linear-gradient(180deg,#e9cdb9 0%,#d9ad95 60%,#e6c3ad 100%)}
  .detail--profile{top:608px;background:linear-gradient(120deg,#ffffff 0%,#f1e7d6 45%,#e5c2ab 100%)}

  /* right column: cover */
  .cover{position:absolute;left:800px;top:0;width:400px;height:848px;background:var(--white)}
  .band{position:absolute;top:0}
  .band--magenta{left:16px;width:17px;height:742px;background:var(--magenta)}
  .band--black{left:46px;width:22px;height:533px;background:var(--black)}
  .cover-title{position:absolute;left:42px;top:824px;transform-origin:0 0;transform:rotate(-90deg);white-space:nowrap;font-family:"Comfortaa",sans-serif;font-size:30px;font-weight:400;line-height:1;color:var(--black)}
  .cover-title .accent{color:var(--magenta)}
  .cover-photo{position:absolute;left:73px;top:70px;width:327px;height:778px;background:linear-gradient(180deg,var(--hair-blond) 0%,var(--skin-light) 22%,var(--skin-mid) 32%,var(--dress-plum) 45%,#6c5c6a 100%)}
  .brand{position:absolute;left:196px;top:16px;display:flex;align-items:center;gap:8px;font-family:"Comfortaa",sans-serif;font-weight:600;font-size:40px;color:var(--black);line-height:1}
  .brand-dot{width:12px;height:12px;border-radius:50%;background:var(--black)}
  .stars-right{position:absolute;left:90px;top:620px}
</style>
</head>
<body>
<main class="flyer">

  <section class="profile">
    <h2 class="profile-name">lena hartmann</h2>
    <div class="portrait" role="img" aria-label="Porträtfoto der Visagistin mit dunklem Kurzhaarschnitt und schwarzer Jacke"></div>
    <div class="portrait-reflection"></div>
    <svg class="stars-left" width="220" height="150" viewBox="0 0 220 150" aria-hidden="true">
      <polygon points="60,10 76,52 120,55 86,80 98,122 60,97 22,122 34,80 0,55 44,52" fill="var(--star-grey)" opacity=".85" transform="rotate(-12 60 66)"/>
      <polygon points="140,0 152,32 188,34 160,54 170,88 140,68 110,88 120,54 92,34 128,32" fill="var(--star-grey)" transform="rotate(14 140 44)"/>
    </svg>
    <div class="profile-text">
      <p>ich habe mich für den beruf friseur entschieden, weil ich es schon immer faszinierend gefunden habe, wie man mit kleinen tricks menschen ganz anders aussehen lassen kann. ich habe schon immer gerne vorher/nachher- sendungen gesehen und bin nach wie vor begeistert, wenn ich meinen kunden und kundinnen mit ein paar handgriffen und tipps ein ganz neues lebensgefühl geben kann.</p>
      <p>am meisten gefällt mir an meinem beruf die vielfalt. oft werde ich gefragt ob ich lieber kurze oder lange, lockige oder glatte haare style. ich kann nur sagen: ich liebe die abwechslung! jeder kunde ist eine neue herausforderung die ich gerne an&shy;nehmen. und auch die verschiedenen bereiche des berufs sind vielfältig. neben meinem friseurberuf bin ich auch visagistin, arbeite für frisurenshows, fotoshootings und als trainerin für andere friseure.</p>
      <p>lockenglanz bedeutet für mich die möglichkeit mit dem eigenen salon neue standards zu schaffen. meine ziele sind eine quali&shy;tativ hochwertige ausbildung der lehrlinge, ein durchdachter rundum-service für unsere kunden, tolle aufstiegschancen für stylisten, anspruchsvolle dienstleistungen und nicht zuletzt:</p>
    </div>
  </section>

  <div class="rule rule--magenta"></div>
  <div class="rule rule--white"></div>

  <section class="details">
    <div class="detail detail--lips" role="img" aria-label="Nahaufnahme glänzender nudefarbener Lippen"></div>
    <div class="detail detail--eyes" role="img" aria-label="Nahaufnahme geschlossener Augen mit schwarzem Lidstrich"></div>
    <div class="detail detail--profile" role="img" aria-label="Seitenprofil eines Models mit blonden Locken und Make-up"></div>
  </section>

  <section class="cover">
    <div class="band band--magenta"></div>
    <div class="band band--black"></div>
    <div class="cover-photo" role="img" aria-label="Model mit platinblonden Locken in einem pflaumenfarbenen Kleid"></div>
    <div class="brand"><span class="brand-dot"></span>mira</div>
    <svg class="stars-right" width="210" height="170" viewBox="0 0 210 170" aria-hidden="true">
      <polygon points="70,10 88,58 138,61 99,90 113,138 70,110 27,138 41,90 2,61 52,58" fill="var(--white)" opacity=".45"/>
      <polygon points="170,20 182,52 216,54 190,74 199,108 170,88 141,108 150,74 124,54 158,52" fill="var(--white)" opacity=".35"/>
    </svg>
    <h1 class="cover-title"><span class="accent">mira</span> beauty schule</h1>
  </section>

</main>
</body>
</html>
```